International Employee Benefits

Create website including logo for Halvorsen Global
Specialising in setting up and managing employee benefits for multi-national companies
Should be professional and simple to navigate
Updates

Company name is Halvorsen Global

Please ensure the following is adhered to :

Page size - 950 pixels wide

If you plan to use a texture or picture background please ensure these are tiled so that the left edge matches the right edge like wallpaper.

The home page should have the logo at the top left of the screen followed by tabs "About Us", "Resources" "Expertise" "References" "Contact Us"
Perhaps there can also be an image on the home page, something that signifies global success??

The wording on the home page should be:

 Halvorsen Global brings a results oriented approach partnering with clients in mapping out customized strategies that meet their international objectives that save time and money and leaves an established process in place.  The client is supported with a high touch, one point of contact, that bring solutions to complex problems

 

Target Market(s)

Companies - HR and Finance

Industry/Entity Type

Employee

Requirements
Must have
• Map of world or globe

```html
<!DOCTYPE html>
<html lang="en">
<head>
<meta charset="utf-8">
<title>Halvorsen Global</title>
<link href="https://fonts.googleapis.com/css2?family=Fjalla+One&family=Open+Sans:wght@400;600&display=swap" rel="stylesheet">
<style>
  :root {
    --page-bg: #f1f1f1;
    --card-bg: #ffffff;
    --brand-blue: #1a73e0;
    --link-blue: #1a9ad6;
    --heading: #3d3d3d;
    --body: #555555;
    --muted: #d0d0d0;
    --rule: #e2e2e2;
    --social-a: #3fa9e0;
    --social-b: #4a5f9a;
    --social-c: #f08a3c;
  }
  * { box-sizing: border-box; margin: 0; padding: 0; }
  html, body { width: 1130px; height: 1200px; overflow: hidden; background: var(--page-bg); }
  body { position: relative; font-family: "Open Sans", sans-serif; color: var(--body); }
  a { color: var(--link-blue); text-decoration: none; }
  .card {
    position: absolute; left: 118px; top: 29px; width: 895px; height: 1143px;
    background: var(--card-bg); border-radius: 6px;
    box-shadow: 0 1px 6px rgba(0,0,0,.12);
  }
  .card > * { position: absolute; }
  .brand { left: 68px; top: 30px; display: flex; align-items: center; gap: 12px; }
  .brand-mark { width: 34px; height: 34px; background: var(--brand-blue); }
  .brand-name { font-size: 29px; font-weight: 400; color: #1b1b1b; letter-spacing: -.3px; }
  .main-nav { right: 52px; top: 58px; display: flex; font-size: 12.5px; color: #333; }
  .main-nav a { color: #333; padding: 0 16px; border-left: 1px solid #ccc; line-height: 14px; }
  .main-nav a:first-child { border-left: 0; }
  .main-nav a:last-child { padding-right: 0; }
  .main-nav a.current { color: var(--link-blue); padding-left: 0; }
  .hero { left: 52px; top: 98px; width: 790px; height: 315px;
    background: radial-gradient(ellipse at 50% 45%, #3fa3f2 0%, #1c6fe0 55%, #0d3fb0 100%); }
  .feature { top: 444px; width: 173px; }
  .feature-photo { width: 173px; height: 97px; }
  .feature h2 { font-family: "Fjalla One", sans-serif; font-weight: 400; font-size: 19px; color: var(--heading); margin-top: 15px; }
  .feature p { font-size: 10.3px; line-height: 14px; margin-top: 8px; width: 180px; }
  .feature a { display: block; font-size: 12px; margin-top: 11px; }
  .section-title { font-family: "Fjalla One", sans-serif; font-weight: 400; font-size: 22px; color: var(--heading); }
  .who { left: 57px; top: 716px; width: 370px; }
  .who-photo { width: 360px; height: 109px; margin-top: 19px; background: linear-gradient(90deg,#c9a58c,#e8d7cc 50%,#b8bcc4); }
  .who p { font-size: 9.6px; line-height: 17px; margin-top: 6px; }
  .who a { display: block; font-size: 12px; margin-top: 10px; }
  .news { left: 461px; top: 716px; width: 380px; }
  .news-item { position: absolute; left: 0; display: flex; gap: 14px; }
  .news-date { font-family: "Fjalla One", sans-serif; font-size: 22px; color: var(--muted); width: 50px; line-height: 24px; }
  .news-item h3 { font-size: 9.6px; font-weight: 400; color: var(--link-blue); text-transform: uppercase; margin-top: 3px; }
  .news-item p { font-size: 9.6px; line-height: 17px; margin-top: 2px; width: 310px; }
  .footer-rule { left: 55px; top: 1053px; width: 778px; height: 1px; background: var(--rule); }
  .copyright { left: 55px; top: 1069px; font-size: 9.6px; color: #666; }
  .social { left: 724px; top: 1067px; display: flex; gap: 5px; }
  .social span { width: 30px; height: 30px; border-radius: 50%; display: block; box-shadow: 0 1px 2px rgba(0,0,0,.2); }
</style>
</head>
<body>
<div class="card">
  <div class="brand"><span class="brand-mark"></span><span class="brand-name">Halvorsen Global</span></div>
  <nav class="main-nav">
    <a class="current" href="#">About Us</a><a href="#">Resources</a><a href="#">Expertise</a><a href="#">References</a><a href="#">Contact Us</a>
  </nav>
  <div class="hero" role="img" aria-label="Businessman in front of a blue world map with silhouettes of colleagues"></div>

  <div class="feature" style="left:53px">
    <div class="feature-photo" role="img" aria-label="Businesswoman smiling at her desk" style="background:linear-gradient(90deg,#e9e3d6,#d8c5b3 60%,#4a4a4a)"></div>
    <h2>Innovation</h2>
    <p>Lorem ipsum dolor sit amet, consectetur adipisicing elit, sed do eiusmod tempor incididunt ut labore et dolore mag.</p>
    <a href="#">Read More</a>
  </div>
  <div class="feature" style="left:258px">
    <div class="feature-photo" role="img" aria-label="Two colleagues shaking hands" style="background:linear-gradient(90deg,#8a6a55,#c8ccd6 50%,#5d6c8a)"></div>
    <h2>Experience</h2>
    <p>Lorem ipsum dolor sit amet, consectetur adipisicing elit, sed do eiusmod tempor incididunt ut labore et dolore mag.</p>
    <a href="#">Read More</a>
  </div>
  <div class="feature" style="left:463px">
    <div class="feature-photo" role="img" aria-label="Smiling young businessman" style="background:linear-gradient(90deg,#e6e6e6,#d9b79d 50%,#c6d4e4)"></div>
    <h2>Solutions</h2>
    <p>Lorem ipsum dolor sit amet, consectetur adipisicing elit, sed do eiusmod tempor incididunt ut labore et dolore mag.</p>
    <a href="#">Read More</a>
  </div>
  <div class="feature" style="left:669px">
    <div class="feature-photo" role="img" aria-label="Team of six colleagues standing together" style="background:linear-gradient(90deg,#d5a9a9,#e4d5d0 50%,#8c8c96)"></div>
    <h2>Support</h2>
    <p>Lorem ipsum dolor sit amet, consectetur adipisicing elit, sed do eiusmod tempor incididunt ut labore et dolore mag.</p>
    <a href="#">Read More</a>
  </div>

  <section class="who">
    <h2 class="section-title">Who We Are</h2>
    <div class="who-photo" role="img" aria-label="Smiling team of colleagues"></div>
    <p>Halvorsen Global brings a results oriented approach partnering with clients in mapping out customized strategies that meet their international objectives that save time and money and leaves an established process in place.&nbsp; The client is supported with a high touch, one point of contact, that bring solutions to complex problems</p>
    <a href="#">Read More</a>
  </section>

  <section class="news">
    <h2 class="section-title">Recent News</h2>
    <div class="news-item" style="top:47px">
      <div class="news-date">05/02</div>
      <div><h3>Lorem ipsum dolor amet consectetur</h3><p>Adipis nullam consequat scelerisque urna, sed sollicitudin elit lobortis varius. Suspendisse ac venenatis velit.</p></div>
    </div>
    <div class="news-item" style="top:115px">
      <div class="news-date">25/01</div>
      <div><h3>Lorem ipsum dolor amet consectetur</h3><p>Adipis nullam consequat scelerisque urna, sed sollicitudin elit lobortis varius. Suspendisse ac venenatis velit.&nbsp; sollicitudin elit lobortis varius. Suspendisse ac venenatis velit.</p></div>
    </div>
    <div class="news-item" style="top:202px">
      <div class="news-date">20/01</div>
      <div><h3>Lorem ipsum dolor amet consectetur</h3><p>Adipis nullam consequat scelerisque urna, sed sollicitudin elit lobortis varius. Suspendisse ac venenatis velit.</p></div>
    </div>
  </section>

  <div class="footer-rule"></div>
  <div class="copyright">Halvorsen Global © 2013.&nbsp; All rights reserved</div>
  <div class="social">
    <span style="background:var(--social-a)"></span>
    <span style="background:var(--social-b)"></span>
    <span style="background:var(--social-c);margin-left:6px"></span>
  </div>
</div>
</body>
</html>
```